Spa brochure design

I need a brochure for my day spa boutique

Here is a new and approved services I do I took it from my website....

Velvet Meadow Signature Facials are customized for all skin types, they include steam, cleanse, tone, exfoliate, extractions, massage of neck, shoulders, head, hands and arms, masque, serum, moisturizer and sun protect...your skin will be radiant, healthy and glowing.  You will instantly notice the difference in the overall tone and texture of your skin. (60 mins) add on a Micro Dermabrasion, Peel or both.  Treatments and Services we provide are:

 

Velvet Meadow Facials 

Velvet Meadow Signature Facials:

Our Signature Facial is 60 minutes of pure heaven for only $60.00  - add on a Micro Dermabrasion, a Peel or both for just $30.00 each.

Velvet Meadow Oxygen Facials:

The Oxygen Facial can give you a detoxifying facial which is excellent for clearing pollutants and toxins from the skin thus improving cell function and increasing oxygen intake it achieve complete, immediate and visible results absolutely perfect for those who have an event to go to. Deep lines and visible wrinkles fade with regular treatment. (75 min) $130.00 

Velvet Meadow Oxygen Micro Facial:

This treatment can give you a detoxifying Oxygen Facial which is excellent for clearing pollutants and toxins from the skin thus improving cell function and increasing oxygen intake. It combines the healing effects of oxygen and serum into one treatment by boosting oxygen levels, the result is a younger, fresher looking skin this plus regular stimulation and micro-circulation of needed exfoliation aids in the production of new collagen and elastinformulation and achieve complete, immediate and visible results deep lines and visible wrinkles fade with regular treatment. $175.00  

Velvet Meadow Back Facial:

A soothing and relaxing treatment for the back especially helps with breakouts and gets rid of impurities where you can't always reach includes cleanse, tone, steam, exfoliate, extractions, masque, moisturizer and sun protection. (45 min) $45.00

Facial on the Rocks:

A Velvet Meadow Signature Facial with added warm stones that makes it that much more relaxing.
(60 min)  $95.00

Teen or On the Go Facial:

Cleansing of the skin, steam, extractions, masque, moisturizer, sun protection (30 min) $45.00

 Add on to any Facial Enzyme Treatment or Specialty Masque $10.00 

Microdermabrasion & Facial Peels

Renewal Microdermabrasion Facial:

A beautiful anti aging treatment that is a exfoliating and resurfacing treatment geared towards those with hyper-pigmentation, fine lines and wrinkles includes: A customized facial for all skin types also face, neck and shoulder massage. (70 min)  $90.00

Renewal Microdermabrasion Treatment:

exfoliating treatment that is a resurfacing treatment, perfect for those with larger pores, hyper-pigmentation,fine lines, and wrinkles also helps with elasticity includes: cleansing, a masque, moisturizer, and sun protection.
(30 min) $60.00

Rejuvenate Glycolic Acid Peel Treatment:

Perfect for normal to dry skin types intensive but safe treatment designed to rapidly exfoliate skin cells, reduces appearance of fine lines, wrinkles and sun damage includes: cleansing, masque, moisturizer, and sun protection. (30 min)  $55.00

Rejuvenate Salicylic Acid Peel Treatment:

Great for oily or acne skin types. This peel exfoliates the pores to allow natural oil production and helps to get sebum production under control includes: cleansing, masque, moisturizer and sun protection. (30 min)  $55.00

Velvet Meadow Massage

Swedish Massage (60 min, 70 min and 90 min)
Aromatherapy Massage $75.00
Deep Tissue Massage $80.00
Pregnancy Massage $70.00
Massage on the Rocks $90.00

Stress Relief Treatment:

A Deep Massage of the Neck, Shoulders and Scalp (15 min) $15.00 (add on to any facial for a $1.00 a minute)

Happy Feet:

Massage and Reflexology of your tired feet (30 min) $30.00  

Waxing Services

Eye Brow Shaping and Trimming  $15.00
Eye Brow Clean-Up $10.00
Lip or Chin $10.00
Face Wax (lip/brow shaping/ chin) $30.00
Side Burns $15.00
Arm Wax:  1/2 arm $25.00 Full are $50.00
Under Arm $25.00
Bikini Wax Starting at $30.00+
Legs 1/2 $30.00+ Full legs $50+
Back Wax $50+

Nail Treatments

Manicure
Pedicure
Foot Detox
Silk Wrap
Hand and Foot Massage and Mask Treatment
Gel Nail 
Polinova Frenchie Manicure $40.00
Polinova Manicure  $35.00
Polinova Pedicure $50.00
Polinova Frenchie Pedicure $60.00
Manicure on the Rocks

Add to any Nail Service:  Polinova $10.00Frenchie $6.00, Hand polish change $8.00, Cut down $2.00, Toe polish change $12.00, One nail repair $5.00, Paraffin Hand Treatment $10.00Foot Treatment $15.00

Eye Lash Treatments

Eye Lash Tinting:

Make your own lashes stand out  "No more fake lashes and glue stuck to your eyes" (30 min) $30.00

Eye Brow Tinting:

Make your brows look Perfect 'No more penciling them in" (30 min) $20.00

For Both Eye Lash and Eye Brow Tinting:

$40.00

Here's my packages....

Velvet Meadow Signature Facials are customized for all skin types, they include steam, cleanse,tone, exfoliate, extractions, massage of neck, shoulders, head, hands and arms, masque, serum, moisturizer and sun protect...your skin will be radiant, healthy and glowing.  You'll instantly notice the difference in the overall tone and texture of you skin. (60 mins) add on a Microdermabrasion, Peel, or both.  Book in for one of beautiful Treatment Packages or Purchase a Treatment Package below as a gift, our treatments include:

Nora Whitcombe Package:

Our 75 minute Swedish Massage combined with both a hand paraffin treatment and a foot detox treatment for a revitalizing experience valued at $225.00 now only $125.00.

Lillian Garroway Package:

Enjoy a Luxury Spa Manicure then a Spa Pedicure at the same time, as a Quillora Botanic Signature Facial that will stimulate all your senses head to toe, and a Stress relief Treatment our regular price is valued at $220.00 now only $170.00.

Rosalind Tepper Package:

Our ultimate Relaxing Pearl Drift Package is our  favorite treatment combined together into one Package includes an Oxygen Facial,  Spa Manicure, Pedicure, and a 60 minute Swedish Massage is valued at $300.00 now only $210.00.

Industry/Entity Type

Boutique

Font styles to use
Serif
Decorative
Script

Requirements
Must have
• My spa and boutiques service,prices, products we use and retail, logo,and have purple and white for colors on brochure.

```html
<!DOCTYPE html>
<html lang="en">
<head>
<meta charset="utf-8">
<title>Velvet Meadow Brochure</title>
<link href="https://fonts.googleapis.com/css2?family=Arimo:ital,wght@0,400;0,700;1,400&display=swap" rel="stylesheet">
<style>
  :root {
    --purple: #7a3e9d;
    --purple-deep: #5e2a7e;
    --lavender: #e6d9ef;
    --ink: #2b2b2b;
    --muted: #6d6d6d;
    --paper: #ffffff;
    --stage: #eeeef0;
    --towel: #d9d6d2;
    --stone: #6f706c;
    --skin: #e9c4ad;
  }
  * { box-sizing: border-box; margin: 0; padding: 0; }
  html, body { width: 1200px; height: 905px; overflow: hidden; }
  body {
    background: var(--stage);
    font-family: "Arimo", Arial, sans-serif;
    color: var(--ink);
    position: relative;
  }
  .spread {
    position: absolute; left: 40px; top: 100px;
    width: 780px; height: 705px;
    display: flex; background: var(--paper);
    box-shadow: 0 4px 18px rgba(0,0,0,.12);
  }
  .panel {
    width: 260px; height: 100%;
    position: relative; overflow: hidden;
    border-right: 1px solid #ececec;
  }
  .panel:last-child { border-right: none; }

  /* packages panel */
  .packages { padding: 28px 18px 0; }
  .packages .photo-bg {
    position: absolute; left: 0; right: 0; bottom: 0; height: 330px;
    background: linear-gradient(160deg, #cfc9c4 0%, #efece8 35%, #8f8f8a 70%, #4d4e4b 100%);
  }
  .kicker { font-size: 8px; font-weight: 700; color: var(--ink); margin-bottom: 8px; padding-left: 8px; }
  .section-title { font-size: 14px; font-weight: 700; color: var(--purple); letter-spacing: .3px; }
  .packages .section-title { padding-left: 8px; margin-bottom: 30px; }
  .package {
    position: relative; z-index: 1;
    background: var(--paper);
    border: 2px solid var(--purple);
    padding: 22px 10px 10px;
    margin-bottom: 48px;
    font-size: 8px; line-height: 1.35; text-align: center;
  }
  .package:nth-of-type(2) { margin-left: 22px; margin-right: -6px; }
  .package:nth-of-type(3) { margin-left: 30px; margin-right: -10px; }
  .package .portrait {
    position: absolute; top: -22px; left: 50%; transform: translateX(-50%);
    width: 38px; height: 38px; border-radius: 50%;
    background: radial-gradient(circle, #bdbdbd, #5a5a5a);
    border: 2px solid var(--paper);
  }
  .package h3 { font-size: 9px; color: var(--purple); margin-bottom: 3px; }
  .package .price { color: var(--purple); font-weight: 700; }

  /* services panels */
  .services { padding: 0 16px; }
  .half-photo {
    width: 130px; height: 62px; margin: 0 auto 14px;
    border-radius: 0 0 65px 65px;
    background: linear-gradient(120deg, #f3ece7, var(--skin) 55%, #f7f4f1);
  }
  .services h2 { font-size: 12px; font-weight: 700; color: var(--purple); margin: 10px 0 4px; }
  .services h3 { font-size: 9px; font-weight: 700; color: var(--purple); margin: 7px 0 2px; }
  .services p { font-size: 7px; line-height: 1.35; color: var(--ink); }
  .services .intro { font-style: italic; color: var(--muted); }
  .services hr { border: none; border-top: 1px solid var(--purple); margin-top: 5px; }
  .services .bottom-photo {
    position: absolute; left: 0; right: 0; bottom: 0; height: 120px;
    background: linear-gradient(170deg, #d8d4cf, #7b7c78 60%, #e8dfb6);
  }
  .services .bottom-card {
    position: relative; z-index: 1; background: var(--paper);
    margin: 0 -16px; padding: 0 16px 8px;
  }
  .list { font-size: 7px; line-height: 1.45; }

  /* cover */
  .cover {
    position: absolute; left: 880px; top: 100px;
    width: 260px; height: 705px; background: var(--paper);
    box-shadow: 0 4px 18px rgba(0,0,0,.12); overflow: hidden;
  }
  .cover svg.art { position: absolute; left: 0; top: 0; }
  .brand {
    position: absolute; left: 0; right: 0; top: 470px;
    display: flex; align-items: center; justify-content: center; gap: 8px;
  }
  .brand-dot { width: 12px; height: 12px; border-radius: 50%; background: var(--purple); }
  .brand-name { font-size: 24px; font-weight: 700; color: var(--purple-deep); }
  .web {
    position: absolute; left: 0; right: 0; top: 585px;
    text-align: center; font-size: 9px; font-weight: 700; color: var(--purple);
  }
  .cover-foot {
    position: absolute; left: 0; right: 0; bottom: 0; height: 70px;
    background: linear-gradient(to bottom, var(--paper), var(--lavender) 50%, #a77dc2);
  }
</style>
</head>
<body>

<section class="spread">
  <div class="panel packages">
    <div class="photo-bg" role="img" aria-label="Photo of rolled white towels, spa stones and purple iris flowers"></div>
    <p class="kicker">Gift Card and Packages Available</p>
    <h2 class="section-title">TREATMENT PACKAGES</h2>
    <article class="package">
      <div class="portrait" role="img" aria-label="Vintage portrait photo"></div>
      <h3>Nora Whitcombe Package</h3>
      <p>Our 75 minute Swedish Massage combined with both a hand paraffin treatment and a foot detox treatment for a revitalizing experience now only <span class="price">$125.00.</span></p>
    </article>
    <article class="package">
      <div class="portrait" role="img" aria-label="Vintage portrait photo"></div>
      <h3>Lillian Garroway Package</h3>
      <p>Enjoy a Luxury Spa Manicure then a Spa Pedicure at the same time, as a Quillora Botanic Signature Facial that will stimulate all your senses head to toe, and a Stress relief Treatment <span class="price">$170.00.</span></p>
    </article>
    <article class="package">
      <div class="portrait" role="img" aria-label="Vintage portrait photo"></div>
      <h3>Rosalind Tepper Package</h3>
      <p>Our ultimate Relaxing Pearl Drift Package is our favorite treatments combined together into one Package, a Oxygen Facial, Spa Manicure, Pedicure, and a 60 min. Swedish Massage. $300 value for <span class="price">$210.00.</span></p>
    </article>
  </div>

  <div class="panel services">
    <div class="bottom-photo" role="img" aria-label="Photo of stacked spa stones and oil bottle"></div>
    <div class="bottom-card">
      <div class="half-photo" role="img" aria-label="Photo of a facial mask being applied"></div>
      <h2 class="section-title">OUR SERVICE</h2>
      <p class="intro">Velvet Meadow Signature Facials are customized for all skin types, they include steam, cleanse, tone, exfoliate, extractions, massage of neck, shoulders, head, hands and arms, masque, serum, moisturizer and sun protect...your skin will be radiant, healthy and glowing. You will instantly notice the difference in the overall tone and texture of your skin. (60 mins) add on a Micro Dermabrasion, Peel or both.</p>
      <h2>Velvet Meadow Facials</h2>
      <h3>Velvet Meadow Signature Facials:</h3>
      <p>Our Signature Facial is 60 minutes of pure heaven for only $60.00 add on a Micro Dermabrasion, a Peel or both for just $30.00 each.</p>
      <hr>
      <h3>Velvet Meadow Oxygen Facials:</h3>
      <p>The Oxygen Facial can give you a detoxifying facial which is excellent for clearing pollutants and toxins from the skin thus improving cell function and increasing oxygen intake it achieve complete, immediate and visible results absolutely perfect for those who have an event to go to. Deep lines and visible wrinkles fade with regular treatment. (75 min) $130.00</p>
      <hr>
      <h3>Velvet Meadow Back Facial:</h3>
      <p>A soothing and relaxing treatment for the back especially helps with breakouts and gets rid of impurities where you can't always reach includes cleanse, tone, steam, exfoliate, extractions, masque, moisturizer and sun protection. (45 min) $45.00</p>
      <hr>
      <h3>Facial on the Rocks:</h3>
      <p>A Velvet Meadow Signature Facial with added warm stones that makes it that much more relaxing. (60 min) $95.00</p>
      <hr>
      <h3>Teen or On the Go Facial:</h3>
      <p>Cleansing of the skin, steam, extractions, masque, moisturizer, sun protection (30 min) $45.00</p>
      <p style="margin-top:6px">Add on to any Facial Enzyme Treatment or Specialty Masque $10.00</p>
    </div>
  </div>

  <div class="panel services">
    <div class="half-photo" role="img" aria-label="Photo of a relaxing facial treatment"></div>
    <h2>Microdermabrasion &amp; Facial Peels</h2>
    <h3>Renewal Microdermabrasion Facial:</h3>
    <p>A beautiful anti aging treatment that is a exfoliating and resurfacing treatment geared towards those with hyper-pigmentation, fine lines and wrinkles includes: A customized facial for all skin types also face, neck and shoulder massage. (70 min) $90.00</p>
    <hr>
    <h3>Renewal Microdermabrasion Treatment:</h3>
    <p>A exfoliating treatment that is a resurfacing treatment, perfect for those with larger pores, hyper-pigmentation, fine lines, and wrinkles also helps with elasticity includes: cleansing, a masque, moisturizer, and sun protection (30 min) $60.00</p>
    <hr>
    <h3>Rejuvenate Glycolic Acid Peel Treatment:</h3>
    <p>Perfect for normal to dry skin types intensive but safe treatment designed to rapidly exfoliate skin cells, reduces appearance of fine lines, wrinkles and sun damage includes: cleansing, masque, moisturizer, and sun protection. (30 min) $55.00</p>
    <hr>
    <h3>Rejuvenate Salicylic Acid Peel Treatment:</h3>
    <p>Great for oily or acne skin types. This peel exfoliates the pores to allow natural oil production and helps to get sebum production under control includes: cleansing, masque, moisturizer and sun protection. (30 min) $55.00</p>
    <hr>
    <h2>Velvet Meadow Massage</h2>
    <p class="list">Swedish Massage (60 min, 70 min and 90 min)<br>Aromatherapy Massage $75.00<br>Deep Tissue Massage $80.00<br>Pregnancy Massage $70.00<br>Massage on the Rocks $90.00</p>
    <hr>
    <h3>Stress Relief Treatment:</h3>
    <p>A Deep Massage of the Neck, Shoulders and Scalp (15 min) $15.00 (add on to any facial for a $1.00 a minute)</p>
    <hr>
    <h3>Happy Feet:</h3>
    <p>Massage and Reflexology of your tired feet (30 min) $30.00</p>
  </div>
</section>

<section class="cover">
  <svg class="art" width="260" height="460" viewBox="0 0 260 460">
    <defs>
      <linearGradient id="relaxGrad" x1="0" y1="0" x2="1" y2="1">
        <stop offset="0" stop-color="#f4e6dc"/>
        <stop offset=".5" stop-color="#e7bfa6"/>
        <stop offset="1" stop-color="#c99a80"/>
      </linearGradient>
      <linearGradient id="stoneGrad" x1="0" y1="0" x2="1" y2="0">
        <stop offset="0" stop-color="#e9e7e4"/>
        <stop offset=".45" stop-color="#7d7e79"/>
        <stop offset=".8" stop-color="#dcd9d5"/>
        <stop offset="1" stop-color="#7a4c9a"/>
      </linearGradient>
    </defs>
    <g role="img" aria-label="Photo of a woman relaxing with eyes closed">
      <rect x="0" y="0" width="260" height="200" fill="url(#relaxGrad)"/>
    </g>
    <g role="img" aria-label="Photo of spa stones, white towels and purple iris">
      <path d="M0 200 H260 V330 C200 360 120 360 70 330 C40 312 15 290 0 270 Z" fill="url(#stoneGrad)"/>
    </g>
    <path d="M0 200 C60 190 150 175 260 180 L260 200 C150 195 70 210 0 232 Z" fill="#ffffff"/>
    <path d="M20 240 C80 200 170 188 260 192" fill="none" stroke="var(--purple)" stroke-width="5"/>
    <path d="M0 262 C20 295 60 335 130 345 C180 352 225 340 260 326" fill="none" stroke="#ffffff" stroke-width="4"/>
  </svg>
  <div class="brand">
    <span class="brand-dot"></span>
    <span class="brand-name">Velvet Meadow</span>
  </div>
  <p class="web">www.velvetmeadowboutiquespa.com</p>
  <div class="cover-foot"></div>
</section>

</body>
</html>
```